Design für Wein-Etikett
Zielgruppe
Zielgruppe ist sowohl der traditionelle Weintrinker (der obendrein auf "Blaublütiges" steht), vor allem aber das junge, moderne Weinpublikum, welches die Message verstanden hat: "Traditionelles modern präsentiert".
Aufgabenstellung
Erstellung eines MODERNEN Weinflaschen-Etikettes, obwohl es auf der Tradition eines alten Prinzengeschlecht beruht. Das Etikett soll als Basis für eine künftige Weinlinie dienen, d.h. das Grundlayout bleibt bestehen, der Jahrgang, die Lagenbezeichnung, die Rebsorten und die AP-Nr. (Abfüllbetrieb) werden variieren.

```html
<!DOCTYPE html>
<html lang="de">
<head>
<meta charset="utf-8">
<title>Haus Hohenwald – Weinetiketten</title>
<link rel="stylesheet" href="https://fonts.googleapis.com/css2?family=Cinzel:wght@700&family=Open+Sans:wght@400&display=swap">
<style>
  :root {
    --page-bg: #ffffff;
    --label-bg: #f6f7f9;
    --label-edge: #e2e4e8;
    --pattern-tone: #dfe5ee;
    --pattern-fade: #f6f7f9;
    --mark-tone: #b9b0a8;
    --name-ink: #4a4340;
    --weissburgunder: #1f7fc1;
    --riesling: #3c9a2b;
    --spaetburgunder: #a3154f;
    --band-text: #ffffff;
  }
  * { box-sizing: border-box; margin: 0; padding: 0; }
  html, body {
    width: 962px;
    height: 1200px;
    overflow: hidden;
    background: var(--page-bg);
  }
  .label-line {
    position: absolute;
    top: 425px;
    left: 40px;
    display: flex;
    gap: 36px;
  }
  .wine-label {
    --accent: var(--weissburgunder);
    position: relative;
    width: 270px;
    height: 350px;
    background: var(--label-bg);
    border: 1px solid var(--label-edge);
    box-shadow: 0 2px 8px rgba(0,0,0,0.08);
    overflow: hidden;
  }
  .wine-label--riesling { --accent: var(--riesling); }
  .wine-label--spaetburgunder { --accent: var(--spaetburgunder); }
  .label-pattern {
    position: absolute;
    inset: 0 0 120px 0;
    background:
      radial-gradient(ellipse at 30% 40%, var(--pattern-tone) 0%, transparent 60%),
      radial-gradient(ellipse at 80% 25%, var(--pattern-tone) 0%, transparent 55%),
      linear-gradient(180deg, var(--pattern-tone) 0%, var(--pattern-fade) 100%);
    opacity: 0.8;
  }
  .grape-variety {
    position: absolute;
    top: 54px;
    left: 0;
    right: 0;
    text-align: center;
    font-family: "Cinzel", "Times New Roman", serif;
    font-weight: 700;
    font-size: 21px;
    letter-spacing: 0.2px;
    color: var(--accent);
  }
  .house-mark {
    position: absolute;
    top: 104px;
    left: 95px;
    width: 80px;
    height: 80px;
    border-radius: 50%;
    background: var(--mark-tone);
    opacity: 0.55;
  }
  .house-name {
    position: absolute;
    top: 224px;
    left: 0;
    right: 0;
    text-align: center;
    font-family: "Cinzel", "Times New Roman", serif;
    font-weight: 700;
    font-size: 18px;
    letter-spacing: 1px;
    line-height: 1.3;
    color: var(--name-ink);
  }
  .label-rule {
    position: absolute;
    left: 0;
    right: 0;
    bottom: 24px;
    height: 1px;
    background: var(--accent);
  }
  .label-band {
    position: absolute;
    left: 0;
    right: 0;
    bottom: 4px;
    height: 16px;
    background: var(--accent);
    color: var(--band-text);
    font-family: "Open Sans", Arial, sans-serif;
    font-size: 8.5px;
    line-height: 16px;
    text-align: center;
    letter-spacing: 0.3px;
  }
</style>
</head>
<body>
  <main class="label-line">
    <article class="wine-label wine-label--weissburgunder">
      <div class="label-pattern" role="img" aria-label="Verblasstes Ornament- und Schriftmuster im Hintergrund"></div>
      <h2 class="grape-variety">WEISSBURGUNDER</h2>
      <div class="house-mark"></div>
      <p class="house-name">Haus Hohenwald</p>
      <div class="label-rule"></div>
      <div class="label-band">www.rebenhof-mustertal.de</div>
    </article>

    <article class="wine-label wine-label--riesling">
      <div class="label-pattern" role="img" aria-label="Verblasstes Ornament- und Schriftmuster im Hintergrund"></div>
      <h2 class="grape-variety">RIESLING</h2>
      <div class="house-mark"></div>
      <p class="house-name">Haus Hohenwald</p>
      <div class="label-rule"></div>
      <div class="label-band">www.rebenhof-mustertal.de</div>
    </article>

    <article class="wine-label wine-label--spaetburgunder">
      <div class="label-pattern" role="img" aria-label="Verblasstes Ornament- und Schriftmuster im Hintergrund"></div>
      <h2 class="grape-variety">SPÄTBURGUNDER</h2>
      <div class="house-mark"></div>
      <p class="house-name">Haus Hohenwald</p>
      <div class="label-rule"></div>
      <div class="label-band">www.rebenhof-mustertal.de</div>
    </article>
  </main>
</body>
</html>
```